Business card for massage therapy company called Brook Fern Wellness

Need business card for massage therapy company called Brook Fern Wellness. Would like my logo on the front and the back of the card I have 3 options of logos and you can play with what looks better.

Would like this information displayed on the back of the card:

Marcus Ellery
Licensed Massage Therapist
321-555-0147
brookfern-example.com
brookfern_rest_

```html
<!DOCTYPE html>
<html lang="en">
<head>
<meta charset="UTF-8">
<title>Brook Fern Wellness – Business Card</title>
<link href="https://fonts.googleapis.com/css2?family=Josefin+Sans:wght@300;400&family=Montserrat:wght@400&display=swap" rel="stylesheet">
<style>
  :root {
    --backdrop: #d6d6d6;
    --card: #ffffff;
    --sage: #6b7260;
    --clay: #b5835f;
    --ink: #2b2b2b;
    --shadow: rgba(0, 0, 0, 0.18);
  }
  * { box-sizing: border-box; margin: 0; padding: 0; }
  html, body {
    width: 1200px;
    height: 1018px;
    overflow: hidden;
    background: var(--backdrop);
  }
  .sheet {
    position: relative;
    width: 1200px;
    height: 1018px;
  }
  .card {
    position: absolute;
    left: 250px;
    width: 700px;
    height: 400px;
    background: var(--card);
    box-shadow: 0 14px 34px var(--shadow);
  }
  .card--front { top: 70px; }
  .card--back  { top: 548px; }

  .wordmark {
    display: flex;
    align-items: center;
    gap: 18px;
  }
  .wordmark__dot {
    width: 74px;
    height: 74px;
    border: 2px solid var(--sage);
    border-radius: 50%;
    flex: none;
  }
  .wordmark__name {
    font-family: "Josefin Sans", sans-serif;
    font-weight: 300;
    color: var(--sage);
    text-transform: uppercase;
    letter-spacing: 0.12em;
    line-height: 1.15;
  }

  .card--front .wordmark {
    position: absolute;
    left: 50%;
    top: 50%;
    transform: translate(-50%, -50%);
  }
  .card--front .wordmark__name { font-size: 40px; }

  .holder {
    position: absolute;
    left: 48px;
    top: 52px;
  }
  .holder__name {
    font-family: "Josefin Sans", sans-serif;
    font-weight: 300;
    font-size: 36px;
    letter-spacing: 0.06em;
    color: var(--sage);
    text-transform: uppercase;
  }
  .holder__role {
    font-family: "Josefin Sans", sans-serif;
    font-weight: 300;
    font-size: 20px;
    color: var(--clay);
    margin-top: 6px;
  }

  .card--back .wordmark {
    position: absolute;
    right: 44px;
    top: 150px;
    gap: 14px;
  }
  .card--back .wordmark__dot { width: 56px; height: 56px; }
  .card--back .wordmark__name { font-size: 30px; }

  .contact {
    position: absolute;
    left: 330px;
    top: 250px;
    list-style: none;
    font-family: "Montserrat", sans-serif;
    font-size: 19px;
    color: var(--ink);
  }
  .contact__item {
    display: flex;
    align-items: center;
    gap: 10px;
    margin-bottom: 10px;
  }
  .contact__icon {
    width: 18px;
    height: 18px;
    flex: none;
  }
</style>
</head>
<body>
<main class="sheet">
  <section class="card card--front" aria-label="Card front">
    <div class="wordmark">
      <span class="wordmark__dot"></span>
      <span class="wordmark__name">Brook Fern<br>Wellness</span>
    </div>
  </section>

  <section class="card card--back" aria-label="Card back">
    <div class="holder">
      <h1 class="holder__name">Marcus Ellery</h1>
      <p class="holder__role">Licensed Massage Therapist</p>
    </div>

    <div class="wordmark">
      <span class="wordmark__dot"></span>
      <span class="wordmark__name">Brook Fern<br>Wellness</span>
    </div>

    <ul class="contact">
      <li class="contact__item">
        <svg class="contact__icon" viewBox="0 0 24 24" aria-hidden="true">
          <path fill="#2b2b2b" d="M6.6 10.8a15.1 15.1 0 0 0 6.6 6.6l2.2-2.2c.3-.3.7-.4 1-.2 1.1.4 2.3.6 3.6.6.6 0 1 .4 1 1V20c0 .6-.4 1-1 1A17 17 0 0 1 3 4c0-.6.4-1 1-1h3.5c.6 0 1 .4 1 1 0 1.3.2 2.5.6 3.6.1.3 0 .7-.2 1z"/>
        </svg>
        <span>321-555-0147</span>
      </li>
      <li class="contact__item">
        <svg class="contact__icon" viewBox="0 0 24 24" aria-hidden="true">
          <circle cx="12" cy="12" r="9" fill="none" stroke="#2b2b2b" stroke-width="2"/>
          <path d="M3 12h18M12 3c3 3 3 15 0 18M12 3c-3 3-3 15 0 18" fill="none" stroke="#2b2b2b" stroke-width="1.5"/>
        </svg>
        <span>brookfern-example.com</span>
      </li>
      <li class="contact__item">
        <svg class="contact__icon" viewBox="0 0 24 24" aria-hidden="true">
          <circle cx="12" cy="12" r="9" fill="none" stroke="#2b2b2b" stroke-width="2"/>
        </svg>
        <span>brookfern_rest_</span>
      </li>
    </ul>
  </section>
</main>
</body>
</html>
```